Redesign Mivorly.com Front Landing Page To Give It The Wow Factor Keeping SEO and Page Load Speeds

We need to redesign the landing page of www.mivorly.com to give it the wow factor

It must have exactly the same content, page size (currently 5.04 KB) or (5,156 bytes) and speed of the current site and rank 100/100 with Trelvix.com tools as the page currently does.

This of course is subjective to content - in other words for an outstanding design - leeway will be given - THE WOW FACTOR IS CRITICAL.

THE PAGE MUST BE HTML5 COMPLIANT AND TOTALLY COMPLETE INCLUDING ANY SCRIPTS, CSS ETC, AND READY TO UPLOAD THE HTML PAGE AND CONTENT FOLDER TO THE SERVER WITH NO MODIFICATIONS REQUIRED.

SERVER IS CURRENTLY KORVANT 2008 HUBCORE R2 BUT WILL SHORTLY BE UPGRADED TO KORVANT 2012 HUBCORE R2 SERVER.

The current landing page loads faster that 96 % of the sites on the web according to Trelvix Tools and that is on our current cable line connection that we are using while site is in development.

So we are looking for a fully optimized page that gives a outstanding first impression and SEO optimized.

It must be fully responsive for all screen size and utilize full page design on larger screen sizes.

The logo will remain to be strictly CSS and there are to be no images used on landing page other than the category link pages, all images must be fully optimized yet sharp and crisp.

A CSS content slider may be used to replace the Javascript rotator currently used - example www.glidepanez.com - we do have a licence for that slider

The winner will also be asked to look at the main script page and given priority in a contest for that as well.

Target Market(s)

World Online Trading Advertising and Business Directory Community Members

Industry/Entity Type

Seo

Requirements
Must have
• A feel of community - must be simple and clean.
• HTML5 Compliant
• Fully SEO optimized but not keyword spammed
• Keep the same content and links as existing landing page
• Search must be fully working and same as current options
Nice to have
• A WOW factor CSS slider - not bloated
Should not have
• No flash or any content that would slow down the front landing page Load Times

```html
<!DOCTYPE html>
<html lang="en">
<head>
<meta charset="utf-8">
<title>Mivorly – Auction Classified &amp; Directory Listings</title>
<link rel="stylesheet" href="https://fonts.googleapis.com/css2?family=Roboto:wght@300;400;500;700&display=swap">
<style>
:root{
  --blue:#55b7f0;
  --blue-dark:#3aa6e6;
  --orange:#e05a12;
  --orange-text:#e0601a;
  --page:#ebebeb;
  --panel:#f1f1f1;
  --text:#555;
  --text-dark:#333;
  --line:#d8d8d8;
  --plum:#9b1358;
  --beige:#e2d9c8;
  --beige-dark:#c9b99b;
  --footer:#b9b9b9;
}
*{box-sizing:border-box;margin:0;padding:0}
html,body{width:922px;height:1200px;overflow:hidden}
body{background:var(--page);font-family:'Roboto',sans-serif;color:var(--text);position:relative;font-weight:300}
.abs{position:absolute}

/* top bar */
.topbar{left:0;top:0;width:922px;height:33px;background:#fff;font-size:9.6px;color:#666}
.topbar .region{left:82px;top:10px;letter-spacing:.2px}
.topbar .region b{font-weight:300;margin-left:8px}
.topbar .region .caret{display:inline-block;border:3px solid transparent;border-top:4px solid #666;margin-left:5px;vertical-align:-1px}
.topbar .links{right:82px;top:10px;display:flex}
.topbar .links span{padding:0 12px;border-left:1px solid #777;line-height:12px}
.topbar .links span:first-child{border-left:0}
.topbar .links span:last-child{padding-right:0}

/* header */
.logo{left:82px;top:74px;font-size:24px;font-weight:700;color:var(--blue);letter-spacing:-.3px}
.search{left:185px;top:58px;width:343px;height:32px;background:var(--blue);border-radius:16px;display:flex;color:#fff;font-size:10.8px;align-items:center}
.search .field{width:187px;padding-left:16px;border-right:1px solid #8fd0f5;height:100%;display:flex;align-items:center}
.search .cat{width:124px;padding-left:12px;display:flex;align-items:center;justify-content:space-between;padding-right:10px;height:100%;border-right:1px solid #8fd0f5}
.search .cat i{border:3.5px solid transparent;border-top:4px solid #fff;margin-top:4px}
.search .go{flex:1;display:flex;align-items:center;justify-content:center}
.opt{font-size:11.4px;color:#666;display:flex;align-items:center;gap:8px}
.radio{width:9px;height:9px;border:1px solid #999;border-radius:50%;background:#fff;position:relative}
.radio.on::after{content:"";position:absolute;left:1.5px;top:1.5px;width:4px;height:4px;border-radius:50%;background:var(--blue)}
.check{width:11px;height:11px}

/* nav */
.nav{left:82px;top:143px;width:758px;height:32px;background:var(--blue);color:#fff;font-size:10.2px;display:flex;align-items:center;padding:0 15px}
.nav span{margin-right:27px}
.nav .right{margin-left:auto;display:flex}
.nav .right span{margin-right:0;margin-left:25px;font-size:10.8px}

/* sidebar */
.sidebar{left:82px;top:208px;width:203px;height:745px;background:var(--panel);border:1px solid #ddd}
.sidebar .head{height:33px;background:var(--blue);color:#fff;font-weight:500;font-size:10.6px;display:flex;align-items:center;padding-left:16px;gap:10px;margin:-1px -1px 0}
.cats{list-style:none;padding:17px 0 0 16px}
.cats li{font-size:10.5px;height:21.2px;display:flex;align-items:center;color:#555;font-weight:400}
.cats li::before{content:"›";width:17px;font-size:12px;color:#777;margin-top:-2px}
.cats li.active{color:var(--orange-text)}
.cats li.active::before{color:var(--orange-text)}

.sample{left:82px;width:203px;height:69px;border-radius:2px;display:flex;align-items:center;justify-content:center;color:#fff;font-weight:500;font-size:17px;text-shadow:0 1px 3px rgba(0,0,0,.6)}
.sample.one{top:970px;background:linear-gradient(180deg,#4b6a86,#6b6445 60%,#8c6d3a)}
.sample.two{top:1056px;background:linear-gradient(180deg,#9fb0c0,#d9d6cf 55%,#6f7a82)}

/* hero */
.hero{left:302px;top:208px;width:538px;height:245px;background:var(--beige);border-radius:3px;overflow:hidden}
.hero svg.curve{position:absolute;left:0;top:0}
.hero h1{position:absolute;left:152px;top:13px;font-size:19.5px;font-weight:400;color:var(--blue)}
.hero ul{position:absolute;left:40px;top:32px;list-style:none;color:var(--orange-text);font-weight:700;font-size:14px}
.hero li{height:34.3px}
.hero .machine{position:absolute;left:315px;top:60px;width:215px;height:180px;border-radius:30px 30px 4px 4px;background:linear-gradient(160deg,#c93a3a,#7e1d1d 60%,#333)}

/* tabs */
.tabs{left:302px;top:477px;width:538px;height:33px;display:flex;gap:1px}
.tabs div{flex:1;background:var(--blue);color:#fff;font-weight:500;font-size:12.2px;display:flex;align-items:center;justify-content:center}
.tabs div.on{background:var(--orange)}

/* cards */
.grid{left:302px;top:526px;width:538px;display:grid;grid-template-columns:repeat(3,171px);column-gap:12.5px;row-gap:12px}
.card{height:245px;background:#fff;text-align:center}
.card .pic{height:147px}
.card h3{font-size:11.6px;font-weight:400;color:#444;margin-top:12px}
.card .price{margin:9px 17px 0;border-top:1px solid #e2e2e2;padding-top:10px;font-size:11px;color:var(--orange-text);font-weight:400}
.card .meta{display:flex;justify-content:center;gap:13px;font-size:8.6px;color:#555;margin-top:19px;font-weight:400}
.card .meta span{display:flex;align-items:center;gap:5px}

/* advantage */
.adv{left:302px;top:1044px;width:538px;height:82px;background:#fff;display:flex}
.adv .badge{width:122px;background:var(--plum);color:#fff;font-weight:700;font-size:13.8px;line-height:17px;display:flex;align-items:center;justify-content:center;text-align:center}
.adv .copy{flex:1;display:flex;flex-direction:column;align-items:center;justify-content:center;gap:7px;color:#333;font-size:11.6px;font-weight:400}
.adv .copy b{font-weight:500}
.adv .edge{width:12px;background:var(--plum)}

.footer{left:0;top:1167px;width:922px;height:33px;background:var(--footer);color:#fff;font-size:9.4px;display:flex;align-items:center;justify-content:center;font-weight:400}
</style>
</head>
<body>

<header class="topbar abs">
  <div class="region abs">SELECT YOUR REGION :<b>UNITED STATES</b><span class="caret"></span></div>
  <nav class="links abs"><span>FEATURES</span><span>MAP LISTING</span><span>POST FREE ADD</span><span>POST FREE AUCTION</span></nav>
</header>

<div class="logo abs">Mivorly</div>

<form class="search abs">
  <div class="field">Search...</div>
  <div class="cat">All Categories <i></i></div>
  <div class="go"><svg width="12" height="12" viewBox="0 0 12 12"><circle cx="5" cy="5" r="3.6" fill="none" stroke="#fff" stroke-width="1.8"/><path d="M7.7 7.7 11 11" stroke="#fff" stroke-width="2" stroke-linecap="round"/></svg></div>
</form>

<div class="opt abs" style="left:552px;top:56px">Match Whole Words <span class="radio on"></span></div>
<div class="opt abs" style="left:707px;top:56px">Partial Word Match <span class="radio"></span></div>
<div class="opt abs" style="left:552px;top:79px">Search Titles
  <svg class="check" viewBox="0 0 11 11"><rect x=".5" y="1.5" width="9" height="9" fill="#fff" stroke="#8fc8ea"/><path d="M2.5 5.5 5 8 10.5 1.5" fill="none" stroke="#3aa6e6" stroke-width="1.6"/></svg></div>
<div class="opt abs" style="left:707px;top:77px">Title &amp; Descriptions
  <svg class="check" viewBox="0 0 11 11"><rect x=".5" y="1.5" width="9" height="9" fill="#fff" stroke="#8fc8ea"/><path d="M2.5 5.5 5 8 10.5 1.5" fill="none" stroke="#3aa6e6" stroke-width="1.6"/></svg></div>

<div class="opt abs" style="left:185px;top:105px">Classifieds Only <span class="radio on"></span></div>
<div class="opt abs" style="left:322px;top:105px">Auctions Only <span class="radio"></span></div>
<div class="opt abs" style="left:450px;top:105px">Auctions &amp; Classifieds <span class="radio"></span></div>
<div class="opt abs" style="left:620px;top:105px">Buy Now Auctions <span class="radio"></span></div>

<nav class="nav abs">
  <span>HOME</span><span>ABOUT US</span><span>COMMUNITY</span><span>SITE MAP</span><span>HELP</span><span>CONTACT US</span>
  <div class="right"><span>+ SEARCH</span><span>STORES</span></div>
</nav>

<aside class="sidebar abs">
  <div class="head">
    <svg width="10" height="9" viewBox="0 0 10 9"><path d="M0 1h10M0 4.5h10M0 8h10" stroke="#fff" stroke-width="1.6"/></svg>
    BROWSE ALL CATEGORIES
  </div>
  <ul class="cats">
    <li class="active">Activities &amp; Events</li><li>Antiques &amp; Collectables</li><li>Automotive &amp; Vehicles</li><li>Aviation &amp; Planes</li><li>Boats &amp; Watercraft</li><li>Business Directory</li><li>Business to Business</li><li>Charities &amp; Non Profits</li><li>Clothing &amp; Accessories</li><li>Computing &amp; Networking</li><li>Construction &amp; Logging</li><li>Daily Deals &amp; Services</li><li>Dining-Food &amp; Beverages</li><li>Education &amp; Training</li><li>Electronics &amp; Phones</li><li>Employment &amp; Careers</li><li>Farming &amp; Agriculture</li><li>Heavy Trucks &amp; Trailers</li><li>Home &amp; Garden</li><li>Industrial Machinery</li><li>Jewelry &amp; Watches</li><li>Motorsports &amp; Racing</li><li>Office &amp; Restuarant</li><li>Personal Services</li><li>Photography &amp;Equipment</li><li>Public News &amp; Events</li><li>Real Estate &amp; Rentals</li><li>Resorts Tickets &amp; Travel</li><li>Sporting Goods &amp; Act.</li><li>RV'S Trailers &amp; Access..</li><li>Tools Hand/Power</li><li>Wanted &amp; Barter/Free</li>
  </ul>
</aside>

<div class="sample one abs" role="img" aria-label="Photo of a tractor in a field">SAMPLE ADD</div>
<div class="sample two abs" role="img" aria-label="Photo of a camper truck">SAMPLE ADD</div>

<section class="hero abs">
  <svg class="curve" width="538" height="245" viewBox="0 0 538 245">
    <path d="M60 245 C160 120 360 70 538 95 V245 Z" fill="#d3c6ad"/>
    <path d="M120 245 C230 150 390 120 538 140 V245 Z" fill="#e8e1d3"/>
  </svg>
  <h1>Auction Classified &amp; Directory Listings</h1>
  <ul><li>BUY</li><li>SELL</li><li>TRADE</li><li>WANTED</li><li>FREE ADS</li><li>AUCTIONS</li></ul>
  <div class="machine" role="img" aria-label="Red truck-mounted loader crane"></div>
</section>

<div class="tabs abs">
  <div class="on">FEATURED LISTINGS</div><div>HOTTEST LISTINGS</div><div>RECENT LISTINGS</div><div>ALL NEW LISTINGS</div>
</div>

<main class="grid abs">
  <article class="card"><div class="pic" role="img" aria-label="Pink pig-shaped mailbox" style="background:linear-gradient(135deg,#e9c3b8,#c98f86 60%,#8a7a6e)"></div><h3>Pig Mailbox</h3><div class="price">$ 129.00</div><div class="meta"><span>♥ Favorites</span><span>✆ Contact Member</span></div></article>
  <article class="card"><div class="pic" role="img" aria-label="Rack-mounted cloud server unit" style="background:linear-gradient(180deg,#fff 35%,#9c9c9c 40%,#555 70%,#f2f2f2 85%)"></div><h3>Micro Cloud Server</h3><div class="price">$ 9,637.63</div><div class="meta"><span>♥ Favorites</span><span>✆ Contact Member</span></div></article>
  <article class="card"><div class="pic" role="img" aria-label="Orange horse-shaped mailbox in a garden" style="background:linear-gradient(180deg,#5d7a3c,#e0612a 45%,#b9502a 65%,#6f8a4a)"></div><h3>Horse Mailbox</h3><div class="price">$ 129.00</div><div class="meta"><span>♥ Favorites</span><span>✆ Contact Member</span></div></article>
  <article class="card"><div class="pic" role="img" aria-label="Stack of pink and silver bangles" style="background:linear-gradient(90deg,#ece7e1 40%,#d63f86 70%,#f1dce6)"></div><h3>Indian Bangles</h3><div class="price">$ 129.00</div><div class="meta"><span>♥ Favorites</span><span>✆ Contact Member</span></div></article>
  <article class="card"><div class="pic" role="img" aria-label="Skid steer loader with fabricated attachment on grass" style="background:linear-gradient(180deg,#c7c6b6,#5b5a4e 45%,#8c8b54 75%,#b39a2a)"></div><h3>RT Fabrications</h3><div class="price">$ 9,637.63</div><div class="meta"><span>♥ Favorites</span><span>✆ Contact Member</span></div></article>
  <article class="card"><div class="pic" role="img" aria-label="Hair studio advertisement on black background" style="background:linear-gradient(180deg,#111,#000)"></div><h3>Marlowe Lane Haircuts</h3><div class="price">$ 129.00</div><div class="meta"><span>♥ Favorites</span><span>✆ Contact Member</span></div></article>
</main>

<section class="adv abs">
  <div class="badge">THE MIVORLY<br>ADVANTAGE</div>
  <div class="copy"><span>CHECK OUT WHAT WE OFFERS VS THE OTHER GUYS?</span><b>Get the best service and features for free!!</b></div>
  <div class="edge"></div>
</section>

<footer class="footer abs">All rights reserved : 2015-2016 © Copyright Mivorly.com Your Free No Credit Cards Required Classifieds Site</footer>

</body>
</html>
```